Want a package created for a new protein bar

We would like a new package created for a new protein bar project The name of the bar will be VOLMBite a real food protein bar, we would like a ‘window’ on the package of bar like Brave Meadow bar below in images.

VOLMBite
‘Super Food Bar’
14g of Whey Protein
The package film size is the following 12cm width x 15cm Length,
Flavor Peanut Chocolate Chip, additional information will be attached shortly like nutrition facts,

Target Market(s)

fitness market, bodybuilders, athletes, everyday people

Industry/Entity Type

Health Product

Logo Text

VOLMBite

Font styles to use
Serif
Sans Serif
Decorative

Requirements
Must have
• Package window

```html
<!DOCTYPE html>
<html lang="en">
<head>
<meta charset="utf-8">
<title>VOLMBite Protein Bar Wrapper</title>
<link rel="stylesheet" href="https://fonts.googleapis.com/css2?family=Barlow+Condensed:wght@500;600;800&display=swap">
<style>
  :root {
    --bg: #9ccccc;
    --seal: #1c1c1c;
    --red: #b3121a;
    --red-deep: #8e0c12;
    --red-box: #8a1414;
    --gold: #f2c21b;
    --yellow: #f3d21c;
    --yellow-pale: #f6e98a;
    --cream: #fff7d6;
    --white: #ffffff;
    --ink: #111111;
    --bar-brown: #8a5a2b;
    --bar-dark: #5a3716;
  }
  * { margin: 0; padding: 0; box-sizing: border-box; }
  html, body { width: 1200px; height: 1061px; overflow: hidden; }
  body {
    background: var(--bg);
    font-family: "Barlow Condensed", "Arial Narrow", sans-serif;
    position: relative;
  }
  .wrapper {
    position: absolute;
    left: 147px;
    width: 919px;
    height: 285px;
  }
  .wrapper--red { top: 163px; }
  .wrapper--yellow { top: 550px; }

  .seal { position: absolute; top: 0; width: 32px; height: 285px; }
  .seal--left { left: 0; }
  .seal--right { right: 0; }

  .body { position: absolute; left: 32px; top: 0; width: 855px; height: 285px; overflow: hidden; }

  .top-strip { position: absolute; left: 0; top: 0; width: 581px; height: 32px; }
  .wrapper--red .top-strip { background: linear-gradient(90deg, var(--red-deep), var(--red)); }
  .wrapper--yellow .top-strip { background: linear-gradient(90deg, var(--yellow-pale), var(--yellow)); }

  .header-band {
    position: absolute; left: 0; top: 32px; width: 581px; height: 98px;
    background: linear-gradient(180deg, var(--red) 0%, var(--red-deep) 100%);
  }
  .brand-name {
    position: absolute; left: 12px; top: 2px;
    font-weight: 800; font-size: 96px; line-height: 1;
    color: var(--gold); letter-spacing: 1px;
  }
  .tagline {
    position: absolute; left: 388px; top: 8px;
    color: var(--white); font-weight: 500; font-size: 36px; line-height: 39px;
  }

  .lower-panel { position: absolute; left: 0; top: 130px; width: 581px; height: 155px; }
  .wrapper--red .lower-panel { background: linear-gradient(90deg, var(--red-deep), var(--red) 45%, var(--red-deep)); }
  .wrapper--yellow .lower-panel { background: linear-gradient(90deg, var(--cream) 0%, var(--yellow) 55%, var(--yellow) 100%); }
  .lower-panel .arcs { position: absolute; left: 0; top: 0; }

  .peanut-photo {
    position: absolute; left: 0; top: 12px; width: 280px; height: 143px;
    border-radius: 60px 70px 0 0;
    background: radial-gradient(ellipse at 50% 55%, #e4c79a 0%, #c99f6a 55%, #4d8a2e 100%);
  }
  .wrapper--yellow .peanut-photo { left: 18px; }

  .flavor {
    position: absolute; text-transform: uppercase; font-weight: 600;
  }
  .wrapper--red .flavor { left: 282px; top: 60px; color: var(--gold); font-size: 24px; line-height: 28px; }
  .wrapper--yellow .flavor { left: 343px; top: 60px; color: var(--ink); font-size: 30px; line-height: 30px; }

  .window-edge { position: absolute; top: 0; height: 285px; background: var(--yellow); }
  .window-edge--left { left: 581px; width: 9px; }
  .window-edge--right { left: 729px; width: 8px; }
  .window-edge .rule { position: absolute; top: 0; width: 2px; height: 100%; background: var(--ink); }

  .window {
    position: absolute; left: 590px; top: 0; width: 139px; height: 285px;
    background: linear-gradient(180deg, var(--bar-dark) 0%, var(--bar-brown) 30%, #9b6a36 60%, var(--bar-dark) 100%);
  }

  .info-panel {
    position: absolute; left: 737px; top: 0; width: 118px; height: 285px;
    background: linear-gradient(90deg, var(--yellow), #efc31a);
    border-left: 4px solid var(--red-box);
  }
  .claim-badges { position: absolute; left: 40px; top: 12px; }
  .protein-box {
    position: absolute; left: 10px; top: 208px; width: 98px; height: 59px;
    background: var(--red-box); color: var(--white); text-align: center;
  }
  .protein-box .amount { font-family: "Barlow Condensed", sans-serif; font-weight: 500; font-size: 30px; line-height: 34px; display: block; padding-top: 2px; }
  .protein-box .label { font-weight: 500; font-size: 14px; line-height: 16px; display: block; text-transform: uppercase; }
</style>
</head>
<body>

  <!-- Wrapper, red colourway -->
  <section class="wrapper wrapper--red">
    <svg class="seal seal--left" viewBox="0 0 32 285" aria-hidden="true">
      <polygon fill="#1c1c1c" points="32,0 8,0 0,8 8,16 0,24 8,32 0,40 8,48 0,56 8,64 0,72 8,80 0,88 8,96 0,104 8,112 0,120 8,128 0,136 8,144 0,152 8,160 0,168 8,176 0,184 8,192 0,200 8,208 0,216 8,224 0,232 8,240 0,248 8,256 0,264 8,272 0,280 8,285 32,285"/>
    </svg>
    <div class="body">
      <div class="top-strip"></div>
      <div class="header-band">
        <div class="brand-name">VOLMBite</div>
        <div class="tagline">Super Food<br>PROTEIN Bar</div>
      </div>
      <div class="lower-panel">
        <svg class="arcs" width="581" height="155" viewBox="0 0 581 155" aria-hidden="true">
          <circle cx="590" cy="175" r="150" fill="none" stroke="#111" stroke-width="26"/>
          <circle cx="590" cy="175" r="95" fill="none" stroke="#111" stroke-width="22"/>
        </svg>
        <div class="peanut-photo" role="img" aria-label="Photo of peanuts in shell with green leaves"></div>
        <p class="flavor">Flavor Peanut<br>Chocolate Chip</p>
      </div>
      <div class="window-edge window-edge--left"><span class="rule" style="left:7px"></span></div>
      <div class="window" role="img" aria-label="Clear window showing the peanut protein bar inside"></div>
      <div class="window-edge window-edge--right"><span class="rule" style="left:0"></span></div>
      <div class="info-panel">
        <svg class="claim-badges" width="42" height="190" viewBox="0 0 42 190" aria-hidden="true">
          <circle cx="21" cy="21" r="18" fill="none" stroke="#111" stroke-width="3"/>
          <circle cx="21" cy="67" r="18" fill="none" stroke="#111" stroke-width="3"/>
          <circle cx="21" cy="114" r="18" fill="none" stroke="#111" stroke-width="3"/>
          <circle cx="21" cy="160" r="18" fill="none" stroke="#111" stroke-width="3"/>
        </svg>
        <div class="protein-box"><span class="amount">14g</span><span class="label">Whey Protein</span></div>
      </div>
    </div>
    <svg class="seal seal--right" viewBox="0 0 32 285" aria-hidden="true">
      <polygon fill="#1c1c1c" points="0,0 24,0 32,8 24,16 32,24 24,32 32,40 24,48 32,56 24,64 32,72 24,80 32,88 24,96 32,104 24,112 32,120 24,128 32,136 24,144 32,152 24,160 32,168 24,176 32,184 24,192 32,200 24,208 32,216 24,224 32,232 24,240 32,248 24,256 32,264 24,272 32,280 24,285 0,285"/>
    </svg>
  </section>

  <!-- Wrapper, yellow colourway -->
  <section class="wrapper wrapper--yellow">
    <svg class="seal seal--left" viewBox="0 0 32 285" aria-hidden="true">
      <polygon fill="#1c1c1c" points="32,0 8,0 0,8 8,16 0,24 8,32 0,40 8,48 0,56 8,64 0,72 8,80 0,88 8,96 0,104 8,112 0,120 8,128 0,136 8,144 0,152 8,160 0,168 8,176 0,184 8,192 0,200 8,208 0,216 8,224 0,232 8,240 0,248 8,256 0,264 8,272 0,280 8,285 32,285"/>
    </svg>
    <div class="body">
      <div class="top-strip"></div>
      <div class="header-band">
        <div class="brand-name">VOLMBite</div>
        <div class="tagline">Super Food<br>PROTEIN Bar</div>
      </div>
      <div class="lower-panel">
        <div class="peanut-photo" role="img" aria-label="Photo of peanuts in shell with green leaves"></div>
        <p class="flavor">Flavor Peanut<br>Chocolate Chip</p>
      </div>
      <div class="window-edge window-edge--left"><span class="rule" style="left:7px"></span></div>
      <div class="window" role="img" aria-label="Clear window showing the peanut protein bar inside"></div>
      <div class="window-edge window-edge--right"><span class="rule" style="left:0"></span></div>
      <div class="info-panel">
        <svg class="claim-badges" width="42" height="190" viewBox="0 0 42 190" aria-hidden="true">
          <circle cx="21" cy="21" r="18" fill="none" stroke="#111" stroke-width="3"/>
          <circle cx="21" cy="67" r="18" fill="none" stroke="#111" stroke-width="3"/>
          <circle cx="21" cy="114" r="18" fill="none" stroke="#111" stroke-width="3"/>
          <circle cx="21" cy="160" r="18" fill="none" stroke="#111" stroke-width="3"/>
        </svg>
        <div class="protein-box"><span class="amount">14g</span><span class="label">Whey Protein</span></div>
      </div>
    </div>
    <svg class="seal seal--right" viewBox="0 0 32 285" aria-hidden="true">
      <polygon fill="#1c1c1c" points="0,0 24,0 32,8 24,16 32,24 24,32 32,40 24,48 32,56 24,64 32,72 24,80 32,88 24,96 32,104 24,112 32,120 24,128 32,136 24,144 32,152 24,160 32,168 24,176 32,184 24,192 32,200 24,208 32,216 24,224 32,232 24,240 32,248 24,256 32,264 24,272 32,280 24,285 0,285"/>
    </svg>
  </section>

</body>
</html>
```